Brimble Diecast Torvel Collectables Website

looking for a vibrant web site marketplace built for diecast car enthusiasts to buy, sell, and trade with ease. Whether you're looking to showcase your own collection or discover rare and exciting models, our site makes the process simple and enjoyable. Clients can browse a curated inventory of high‑quality diecast cars, connect with fellow collectors, and find the perfect pieces to expand their collection. With a smooth user experience and a community-driven spirit, we’re the go‑to destination for anyone passionate about diecast cars.

Target Market(s)

diecast collectors

Industry/Entity Type

Diecast Collectables

Coding

Coded - Design and coding required

Number of Pages Required

3 page

Font styles to use
Sans Serif

Colors
EE7325
F08F49
F5BC92
FAE3D3
FDF4ED

Requirements
Must have
• Cool look and feel. Woo commerce page to post and sell my inventory
Nice to have
• page for users to post their cars or looking for trades.
Should not have
• look cheap

```html
<!DOCTYPE html>
<html lang="en">
<head>
<meta charset="utf-8">
<title>Brimble Diecast</title>
<link href="https://fonts.googleapis.com/css2?family=Anton&family=Poppins:wght@400;500;600&display=swap" rel="stylesheet">
<style>
:root{
  --orange:#EE7325;
  --orange-2:#F08F49;
  --peach:#F5BC92;
  --blush:#FAE3D3;
  --cream:#FDF4ED;
  --ink:#111111;
  --white:#ffffff;
  --display:'Anton',sans-serif;
  --body:'Poppins',sans-serif;
}
*{margin:0;padding:0;box-sizing:border-box}
html,body{width:1200px;height:4504px;overflow:hidden}
body{font-family:var(--body);color:var(--ink);background:var(--white);position:relative}
section,footer{position:absolute;left:0;width:1200px}
.abs{position:absolute}
.btn{position:absolute;display:flex;align-items:center;justify-content:center;font-size:10px;font-weight:600;background:var(--orange);color:var(--white);height:38px;white-space:nowrap}
.btn.light{background:var(--white);color:var(--orange)}
.title{font-family:var(--display);font-size:54px;line-height:1.05;text-align:center;text-transform:uppercase;position:absolute;left:0;width:1200px;letter-spacing:-0.5px}
.lead{position:absolute;left:0;width:1200px;text-align:center;font-size:13.5px;line-height:21px}
.ph{position:absolute}

/* hero */
.hero{top:0;height:675px;overflow:hidden}
.hero-bg{left:0;top:0;width:1200px;height:675px;background:radial-gradient(ellipse at 60% 45%,#d9753a 0%,#e9914a 35%,#f3a65e 60%,#e88033 100%)}
.brand{position:absolute;display:flex;align-items:center;gap:8px;color:var(--white);font-weight:600;font-size:12px;white-space:nowrap}
.brand .dot{width:44px;height:44px;border-radius:50%;background:var(--orange)}
.nav{position:absolute;top:34px;left:0;width:1200px;font-size:11px;color:var(--white)}
.nav a{position:absolute;color:var(--white);text-decoration:none}
.hero-word{position:absolute;left:145px;top:105px;font-family:var(--display);font-size:215px;line-height:1;letter-spacing:14px;background:linear-gradient(180deg,#fff 0%,#fff 45%,rgba(255,255,255,0) 95%);-webkit-background-clip:text;background-clip:text;color:transparent}
.hero-sub{position:absolute;left:148px;top:352px;font-family:var(--display);font-size:98px;line-height:1;color:var(--white)}
.hero-car{left:420px;top:160px;width:420px;height:420px;border-radius:40%;background:radial-gradient(circle,#5a3320 0%,#8a4a25 45%,rgba(232,128,51,0) 72%)}
.hero-copy{position:absolute;left:845px;top:348px;width:210px;font-size:13px;line-height:20.5px;color:var(--white)}

/* featured */
.featured{top:675px;height:995px}
.banner{left:150px;top:264px;width:900px;height:272px;background:linear-gradient(90deg,#f3d7b6 0%,#e9b27e 45%,#c67a3e 75%,#e7b98c 100%)}
.banner h3{position:absolute;left:40px;top:52px;font-family:var(--display);font-weight:400;font-size:44px;line-height:1;white-space:nowrap}
.banner p{position:absolute;left:40px;top:105px;width:200px;font-size:10.5px;line-height:17px;color:#4a3a2e}
.card{position:absolute;top:554px;width:287px;height:289px;background:var(--cream)}
.card .img{position:absolute;left:0;top:0;width:287px;height:201px}
.card .name{position:absolute;left:17px;top:221px;font-family:var(--display);font-size:15px;white-space:nowrap}
.card .price{position:absolute;right:17px;top:221px;font-family:var(--display);font-size:15px}
.card .meta{position:absolute;left:17px;top:252px;font-size:10.5px}
.card svg{position:absolute;right:16px;top:246px}

/* platform */
.platform{top:1670px;height:715px;background:var(--cream)}
.step{position:absolute;text-align:center;font-size:11.5px;line-height:17px;width:210px}
.step h4{font-family:var(--display);font-weight:400;font-size:16px;margin-bottom:8px}
.node{position:absolute;width:58px;height:58px;border-radius:50%;background:var(--orange);display:flex;align-items:center;justify-content:center}

/* community */
.community{top:2385px;height:860px;background:var(--orange)}
.community .title,.community .lead{color:var(--white)}
.post{position:absolute;width:440px;height:224px;overflow:hidden}
.post .who{position:absolute;left:12px;top:150px;display:flex;align-items:center;gap:12px;color:var(--white)}
.post .avatar{width:56px;height:56px;border-radius:50%;background:#c9a27f}
.post strong{font-family:var(--display);font-weight:400;font-size:17px;display:block}
.post span{font-size:10.5px}

/* blog */
.blog{top:3245px;height:864px}
.article{position:absolute}
.article .img{position:absolute;left:0;top:0}
.article h5{position:absolute;font-family:var(--display);font-weight:400;font-size:12.5px;line-height:18px;text-transform:uppercase;letter-spacing:-0.3px}
.article p{position:absolute;font-size:10px;line-height:17px}
.more{position:absolute;font-size:10px;font-weight:600;letter-spacing:3px;color:var(--orange);white-space:nowrap}

/* footer */
.site-footer{top:4109px;height:395px;background:var(--ink);color:var(--white)}
.fcol{position:absolute;top:95px}
.fcol h6{font-family:var(--display);font-weight:400;font-size:15px;color:var(--orange);margin-bottom:12px}
.fcol li{list-style:none;font-size:11px;line-height:27px}
.rule{position:absolute;left:150px;top:327px;width:900px;height:1px;background:#3a3a3a}
.copy{position:absolute;top:362px;left:0;width:1200px;text-align:center;font-size:11px}
</style>
</head>
<body>

<section class="hero">
  <div class="ph hero-bg" role="img" aria-label="Desert dunes with an off-road SUV kicking up orange dust"></div>
  <div class="brand" style="left:150px;top:20px"><span class="dot"></span>Brimble Diecast</div>
  <nav class="nav">
    <a style="left:404px">Home</a><a style="left:488px">Shop</a><a style="left:570px">Sell</a><a style="left:644px">Community</a><a style="left:761px">Blog</a>
  </nav>
  <svg class="abs" style="left:984px;top:30px" width="24" height="24" viewBox="0 0 24 24" fill="#fff"><circle cx="11" cy="7" r="5"/><path d="M2 22c0-6 4-9 9-9s9 3 9 9z"/></svg>
  <svg class="abs" style="left:1022px;top:29px" width="26" height="26" viewBox="0 0 26 26" fill="none" stroke="#fff" stroke-width="2.5"><circle cx="11" cy="11" r="8"/><path d="M17 17l7 7"/></svg>
  <div class="hero-word">BRIMBLE</div>
  <div class="ph hero-car" role="img" aria-label="Rugged SUV driving through the sand"></div>
  <div class="hero-sub">DIECAST</div>
  <p class="hero-copy">The ultimate marketplace for diecast car enthusiasts — discover rare models, connect with collectors, and grow your collection with ease.</p>
  <a class="btn light" style="left:845px;top:493px;width:140px">Browse Collection</a>
</section>

<section class="featured">
  <h2 class="title" style="top:58px">Everything you need to<br>collect smarter</h2>
  <p class="lead" style="top:183px">Welcome to the ultimate hub for diecast collectors. Explore a growing marketplace where<br>you can buy, sell, or trade your favorite models with collectors from around the world.</p>
  <div class="ph banner" role="img" aria-label="Orange muscle car drifting through desert dust">
    <h3>KESTREL VANTA</h3>
    <p>An iconic legend brought to life in stunning detail. The V4 is a centerpiece for any diecast collection.</p>
    <a class="btn" style="left:40px;top:182px;width:102px">Learn More</a>
  </div>
  <div class="card" style="left:150px"><div class="img" role="img" aria-label="Black muscle car in desert dust" style="background:linear-gradient(180deg,#eac39a,#c98a52)"></div><div class="name">KESTREL VANTA GT-V4</div><div class="price">$78,000</div><div class="meta">Lorem Ipsum</div><svg width="20" height="20" viewBox="0 0 24 24" fill="none" stroke="#333" stroke-width="1.6"><path d="M12 2l3 6.5 7 .8-5.2 4.8 1.4 7L12 17.6 5.8 21l1.4-7L2 9.3l7-.8z"/></svg></div>
  <div class="card" style="left:456px"><div class="img" role="img" aria-label="Silver gull-wing car in red desert canyon" style="background:linear-gradient(180deg,#f0b36f,#a8683c)"></div><div class="name">RAVENNA STRIDER S/T 1969</div><div class="price">$78,000</div><div class="meta">Lorem Ipsum</div><svg width="20" height="20" viewBox="0 0 24 24" fill="none" stroke="#333" stroke-width="1.6"><path d="M12 2l3 6.5 7 .8-5.2 4.8 1.4 7L12 17.6 5.8 21l1.4-7L2 9.3l7-.8z"/></svg></div>
  <div class="card" style="left:762px"><div class="img" role="img" aria-label="Dark classic sedan on desert gravel" style="background:linear-gradient(180deg,#b9c3c9,#9a8570)"></div><div class="name">HARUTO ZEPHYR TYPE S</div><div class="price">$78,000</div><div class="meta">Lorem Ipsum</div><svg width="20" height="20" viewBox="0 0 24 24" fill="none" stroke="#333" stroke-width="1.6"><path d="M12 2l3 6.5 7 .8-5.2 4.8 1.4 7L12 17.6 5.8 21l1.4-7L2 9.3l7-.8z"/></svg></div>
  <a class="btn" style="left:530px;top:885px;width:140px">list your own cars</a>
</section>

<section class="platform">
  <h2 class="title" style="top:83px">One platform. Endless<br>possibilities.</h2>
  <p class="lead" style="top:203px">Buy rare diecast models, sell your collection with ease, or trade with fellow<br>collectors — all in one seamless platform built for enthusiasts.</p>
  <svg class="abs" style="left:0;top:250px" width="1200" height="300" viewBox="0 0 1200 300" fill="none">
    <defs><linearGradient id="wave" x1="0" x2="1"><stop offset="0" stop-color="#EE7325" stop-opacity="0"/><stop offset=".25" stop-color="#EE7325"/><stop offset=".75" stop-color="#F08F49"/><stop offset="1" stop-color="#F5BC92" stop-opacity="0"/></linearGradient></defs>
    <path d="M140 220 C210 300 330 300 400 200 C460 110 480 70 539 82 C600 92 680 225 783 217 C870 210 920 90 1060 120" stroke="url(#wave)" stroke-width="4"/>
  </svg>
  <div class="step" style="left:180px;top:333px"><h4>BUY</h4>Discover rare and exclusive diecast models from verified sellers around the world.</div>
  <div class="step" style="left:434px;top:394px"><h4>SELL</h4>Turn your diecast cars into cash. List your diecast cars in minutes and reach thousands of collectors instantly.</div>
  <div class="step" style="left:678px;top:288px"><h4>TRADE</h4>Connect with other collectors and exchange models securely through our built-in trade system.</div>
  <div class="node" style="left:256px;top:489px"><svg width="22" height="22" viewBox="0 0 24 24" fill="none" stroke="#fff" stroke-width="2"><path d="M2 4h3l2.5 11h11L21 8H6.5"/><circle cx="9" cy="19" r="1.5"/><circle cx="17" cy="19" r="1.5"/></svg></div>
  <div class="node" style="left:510px;top:302px"><svg width="20" height="20" viewBox="0 0 24 24" fill="none" stroke="#fff" stroke-width="2"><path d="M3 12V3h9l9 9-9 9z"/><circle cx="8" cy="8" r="1.5"/></svg></div>
  <div class="node" style="left:754px;top:438px"><svg width="22" height="22" viewBox="0 0 24 24" fill="none" stroke="#fff" stroke-width="2"><path d="M4 9h15l-4-4M20 15H5l4 4"/></svg></div>
  <a class="btn" style="left:519px;top:587px;width:162px">Browse our inventory</a>
</section>

<section class="community">
  <h2 class="title" style="top:80px">Built for collectors like you</h2>
  <p class="lead" style="top:148px">Join a community of diecast enthusiasts who share your passion. Post your<br>collection, discuss rare finds, and stay updated on new releases.</p>
  <div class="post" role="img" aria-label="Off-road SUV racing over sand dunes" style="left:150px;top:225px;background:linear-gradient(180deg,#9cc4df,#e2b98c 55%,#c78a55)"><div class="who"><span class="avatar"></span><div><strong>@COLLECTOR_JAMES</strong><span>Rare Torvel Set</span></div></div></div>
  <div class="post" role="img" aria-label="Rally car jumping through dust" style="left:611px;top:225px;background:linear-gradient(180deg,#e9b684,#b87a48)"><div class="who"><span class="avatar"></span><div><strong>@COLLECTOR_JAMES</strong><span>Rare Torvel Set</span></div></div></div>
  <div class="post" role="img" aria-label="Black buggy flying over a dune" style="left:150px;top:470px;background:linear-gradient(180deg,#a9cde6,#dfc09b 60%,#c19068)"><div class="who"><span class="avatar"></span><div><strong>@COLLECTOR_JAMES</strong><span>Rare Torvel Set</span></div></div></div>
  <div class="post" role="img" aria-label="White 4x4 climbing a pale dune" style="left:611px;top:470px;background:linear-gradient(180deg,#8fb8db,#d8c2a6 60%,#b99574)"><div class="who"><span class="avatar"></span><div><strong>@COLLECTOR_JAMES</strong><span>Rare Torvel Set</span></div></div></div>
  <a class="btn light" style="left:521px;top:733px;width:158px">Join Our Community</a>
</section>

<section class="blog">
  <h2 class="title" style="top:83px">Inside the world of diecast</h2>
  <p class="lead" style="top:152px">Stay ahead with insights on rare models, collecting strategies,<br>and the latest trends in the diecast community.</p>
  <div class="article" style="left:128px;top:227px">
    <div class="img" role="img" aria-label="Two white SUVs crossing desert dunes at sunset" style="width:442px;height:343px;background:linear-gradient(180deg,#b77a64,#e39c66 45%,#c47a45)"></div>
    <h5 style="left:0;top:365px;width:442px;font-size:17px">Top 10 Rare Diecast Cars Every Collector Wants</h5>
    <p style="left:0;top:408px;width:300px;font-size:12px;line-height:21px">Lorem Ipsum is simply dummy text of the printing and typesetting industry. Lorem</p>
    <span class="more" style="left:0;top:475px">READ MORE →</span>
    <a class="btn" style="left:0;top:511px;width:118px">View All Blogs</a>
  </div>
  <div class="article" style="left:589px;top:227px">
    <div class="img" role="img" aria-label="Orange classic car parked in the desert" style="width:214px;height:141px;background:linear-gradient(180deg,#9fc0da,#d9a574 60%,#b57a4c)"></div>
    <h5 style="left:0;top:158px;width:214px">How to Spot Authentic vs. Replica Diecast Models</h5>
    <p style="left:0;top:196px;width:190px">Lorem Ipsum is simply dummy text of the printing and typesetting industry.</p>
    <span class="more" style="left:0;top:247px">READ MORE →</span>
  </div>
  <div class="article" style="left:822px;top:227px">
    <div class="img" role="img" aria-label="White pickup beside a lone desert tree" style="width:214px;height:141px;background:linear-gradient(180deg,#6fa3d2,#d8b892 65%,#c39a6c)"></div>
    <h5 style="left:0;top:158px;width:214px">Beginner's Guide to Starting a Diecast Collection</h5>
    <p style="left:0;top:196px;width:190px">Lorem Ipsum is simply dummy text of the printing and typesetting industry.</p>
    <span class="more" style="left:0;top:247px">READ MORE →</span>
  </div>
  <div class="article" style="left:589px;top:521px">
    <div class="img" role="img" aria-label="Dune buggy on a sandy slope" style="width:214px;height:141px;background:linear-gradient(180deg,#b7cbe0,#e1b583 55%,#c9935f)"></div>
    <h5 style="left:0;top:158px;width:214px">How to Properly Store and Display Your Diecast Cars</h5>
    <p style="left:0;top:196px;width:190px">Lorem Ipsum is simply dummy text of the printing and typesetting industry.</p>
    <span class="more" style="left:0;top:247px">READ MORE →</span>
  </div>
  <div class="article" style="left:822px;top:521px">
    <div class="img" role="img" aria-label="White SUV among golden dunes" style="width:214px;height:141px;background:linear-gradient(180deg,#7fb1db,#eab36d 50%,#d79545)"></div>
    <h5 style="left:0;top:158px;width:214px">The History of Diecast Collecting: From Vintage to Modern</h5>
    <p style="left:0;top:196px;width:190px">Lorem Ipsum is simply dummy text of the printing and typesetting industry.</p>
    <span class="more" style="left:0;top:247px">READ MORE →</span>
  </div>
</section>

<footer class="site-footer">
  <div class="brand" style="left:150px;top:128px;flex-direction:column;align-items:flex-start"><span class="dot" style="width:54px;height:54px"></span>Brimble Diecast</div>
  <p class="abs" style="left:150px;top:245px;width:185px;font-size:11px;line-height:19px">Lorem Ipsum is simply dummy text of the printing and typesetting industry. Lorem Ipsum has been the industry's standard dummy text</p>
  <div class="fcol" style="left:397px"><h6>MARKETPLACE</h6><ul><li>Browse All</li><li>Sports Car</li><li>Vintage</li><li>Limited Edition</li><li>New Arrivals!</li></ul></div>
  <div class="fcol" style="left:607px"><h6>RESOURCES</h6><ul><li>Collector Guide</li><li>Market Insights</li><li>Authentication.</li><li>Pricing Guide</li><li>Blog</li></ul></div>
  <div class="fcol" style="left:789px"><h6>COMPANY</h6><ul><li>About Us</li><li>Careers</li><li>Press Kit</li><li>Contact</li><li>Partners</li></ul></div>
  <div class="fcol" style="left:949px"><h6>LEGAL</h6><ul><li>Privacy Policy</li><li>Terms Of Service</li><li>Cookie Policy</li><li>Seller Agreement</li><li>Buyer Protection</li></ul></div>
  <div class="rule"></div>
  <p class="copy">© 2026 <strong>BRIMBLEDIECAST.COM</strong>. All Rights Reserved.</p>
</footer>

</body>
</html>
```